Flyer Design Project

Need a creative flyer design for a new coffee shop. The name of the coffee shop is Brisk Kettle. We sell coffees, teas, espresso based drinks, pastries and freshly made mini donuts.
Looking for the flyer to have the following:
1. Now Open
2. advertisement: try our freshly made mini donuts 6 for $1
3. advertisement: 1/2 price coffee Monday's
4. address: 538 north 4th street, Roselle, NJ 07156
5. pictures of coffee and lattes
6. the logo
7. offers end June 30, 2013
8. Free Wifi
Feel free to be creative. I want the flyer to be eye catching. Open to different sizes and shapes to the flyer.
Note: flyer can be one or two sided. I do not have any additional photos.
Coffee Shop

```html
<!DOCTYPE html>
<html lang="en">
<head>
<meta charset="utf-8">
<title>Brisk Kettle – Now Open</title>
<link rel="stylesheet" href="https://fonts.googleapis.com/css2?family=Anton&family=Josefin+Sans:wght@300;400;700&display=swap">
<style>
  :root {
    --paper: #ece6db;
    --paper-edge: #ddd5c7;
    --espresso: #35261b;
    --bean-dark: #4a2a14;
    --bean-mid: #8a5228;
    --bean-light: #b67a45;
    --ink: #2e2620;
    --monday-red: #e31e26;
    --donut-orange: #f0861a;
    --cup-red: #e2392a;
    --cup-orange: #f39a2c;
    --foam: #f6e3b6;
    --donut-tan: #e9dcc6;
    --face-tones: #d7b9a0;
  }
  * { margin: 0; padding: 0; box-sizing: border-box; }
  html, body {
    width: 915px;
    height: 1200px;
    overflow: hidden;
    background: var(--paper);
  }
  .flyer {
    position: relative;
    width: 915px;
    height: 1200px;
    overflow: hidden;
    background: radial-gradient(ellipse at 50% 55%, #f1ece3 0%, var(--paper) 60%, var(--paper-edge) 100%);
    color: var(--ink);
    font-family: "Josefin Sans", "Gill Sans", sans-serif;
  }
  .beans-photo {
    position: absolute;
    left: 0; top: 0;
    width: 915px; height: 340px;
    background:
      radial-gradient(ellipse 130px 85px at 330px 225px, var(--bean-light) 0%, var(--bean-mid) 55%, transparent 75%),
      radial-gradient(ellipse 120px 80px at 770px 240px, var(--bean-light) 0%, var(--bean-mid) 55%, transparent 75%),
      radial-gradient(ellipse 110px 75px at 60px 150px, var(--bean-mid) 0%, var(--bean-dark) 60%, transparent 78%),
      linear-gradient(180deg, var(--bean-dark) 0%, var(--bean-mid) 35%, rgba(138,82,40,0.55) 62%, rgba(236,230,219,0) 100%);
  }
  .headline {
    position: absolute;
    left: 40px; top: 355px;
    width: 840px;
    font-family: "Anton", "Impact", sans-serif;
    font-size: 192px;
    line-height: 1;
    color: var(--espresso);
    letter-spacing: 2px;
    word-spacing: 28px;
    white-space: nowrap;
  }
  .offer-end {
    position: absolute;
    left: 44px; top: 552px;
    font-weight: 700;
    font-size: 46px;
    line-height: 1.2;
    color: var(--espresso);
    white-space: nowrap;
  }
  .deal {
    position: absolute;
    font-weight: 300;
    color: var(--ink);
    white-space: nowrap;
  }
  .deal--coffee {
    right: 357px; top: 639px;
    font-size: 52px;
    line-height: 1.2;
    text-align: right;
  }
  .deal--donuts {
    left: 44px; top: 775px;
    font-size: 47px;
    line-height: 1.4;
  }
  .deal .highlight-red { color: var(--monday-red); font-weight: 400; }
  .deal .highlight-orange { color: var(--donut-orange); font-weight: 400; }
  .perk {
    position: absolute;
    left: 44px; top: 945px;
    font-weight: 700;
    font-size: 40px;
    line-height: 1.2;
    color: var(--espresso);
    white-space: nowrap;
  }
  .latte-illustration {
    position: absolute;
    left: 612px; top: 575px;
    width: 265px; height: 315px;
    border-radius: 40% 40% 30% 30%;
    background: radial-gradient(ellipse at 45% 45%, var(--foam) 0%, var(--cup-orange) 40%, var(--cup-red) 70%, rgba(226,57,42,0) 100%);
  }
  .donut-people-illustration {
    position: absolute;
    left: 425px; top: 900px;
    width: 460px; height: 200px;
    border-radius: 50%;
    background: radial-gradient(ellipse at 20% 50%, var(--cup-orange) 0%, var(--donut-tan) 28%, rgba(233,220,198,0) 55%),
                radial-gradient(ellipse at 75% 45%, var(--face-tones) 0%, rgba(215,185,160,0) 50%);
  }
  .brand {
    position: absolute;
    left: 44px; top: 1060px;
    display: flex;
    align-items: center;
    gap: 12px;
  }
  .brand__dot {
    width: 30px; height: 30px;
    border-radius: 50%;
    background: var(--donut-orange);
  }
  .brand__name {
    font-weight: 700;
    font-size: 38px;
    color: var(--espresso);
    white-space: nowrap;
  }
  .address {
    position: absolute;
    left: 296px; top: 1118px;
    font-weight: 400;
    font-size: 27px;
    letter-spacing: 3px;
    color: var(--ink);
    white-space: nowrap;
  }
</style>
</head>
<body>
<main class="flyer">
  <div class="beans-photo" role="img" aria-label="Close-up photograph of roasted coffee beans"></div>

  <h1 class="headline">NOW OPEN!</h1>
  <p class="offer-end">offers end June 30, 2013</p>

  <p class="deal deal--coffee">1/2 price coffee's<br><span class="highlight-red">Monday's</span></p>
  <p class="deal deal--donuts">Try our freshly made<br><span class="highlight-orange">Mini Donuts</span> 6 for $1</p>

  <p class="perk">Free Wifi</p>

  <div class="latte-illustration" role="img" aria-label="Illustration of a red latte cup with whipped foam and steam"></div>
  <div class="donut-people-illustration" role="img" aria-label="Illustration of a sprinkled mini donut beside three drawn customers"></div>

  <div class="brand">
    <span class="brand__dot"></span>
    <span class="brand__name">Brisk Kettle</span>
  </div>

  <p class="address">538 north 4th street, Roselle, NJ 07156</p>
</main>
</body>
</html>
```